TerraLume Business Card Design Project

We need a business card design for a new company called "TerraLume Systems". TerraLume provides 3D visualization software for subsurface oil and gas data so you can make confident downhole decisions.

Our goal is to provide easy to understand big pictures of your data so your can make confident planning decisions.

Our tagline is
SEAMLESS DATA SHARING. EFFECTIVE COLLABORATION. CONFIDENT DECISION-MAKING

Check out http://www.terralume-example.com for more ideas.

The design should promote a technology company that delivers web-based solutions focused on photo-realistic 3D graphics.

The colors from our existing logo (attached) are one option but not a requirement. The design SHOULD NOT use the existing logo.

The design should be two sided and full color. If you require any special print considerations (example: paper type, matte finish, metallic ink, etc) please provide detailed comments. Please also specify any desired details such as rounding of corners, etc.

IF YOU USE BLACK our printer states "We recommend using CMYK black (0, 0, 0, 100) or for a rich black (60, 40, 40, 100). Ensure your artwork is in CMYK mode before adjusting the black."

For design purposes you can use the following contact information

name: Harlan Pike
title: founder
phone: 555.987.6543
email: harlan@terralume-example.com

company information
TerraLume is our "branded" name
"TerraLume Systems" is our official name
www.terralume-example.com

address:
Suite 720
482 Birchmont Avenue SW
Calgary, AB, Canada
T3K 4R8

Target Market(s)

Companies spend a lot of time collecting, organizing and analyzing data but it's really hard to to get a big picture view of current and planned projects, especially in context to existing wellbores, geology and downhole equipment

TerraLume enables you to explore the big picture in an immersive, 3D environment. Our goal is to help transform you rich data into an easily understood picture, to make confident planning decisions and anticipate trouble events before the expensive execution phase.

Industry/Entity Type

Oil And Gas

Requirements
Must have
• The business card design should be sized to a standard 3.5 x 2 inches and print ready. See the attachment for a sample sized card
It MUST meet these requirements:
Exported as PDF file with two pages:
page 1: front design
page 2: back design
All Images must be 300ppi or higher (at 100%)
CMYK colour mode
0.125 inches of bleed on all sides (0.25 inches additional width and height)
0.125 inch safety margin (inside trim line)

```html
<!DOCTYPE html>
<html lang="en">
<head>
<meta charset="utf-8">
<title>TerraLume Systems – Business Card</title>
<link href="https://fonts.googleapis.com/css2?family=Barlow:wght@400;500;600&display=swap" rel="stylesheet">
<style>
  :root {
    --backdrop: #2a2a2b;
    --card-dark: #58595b;
    --card-light: #eeeeee;
    --ink-dark: #4a4b4d;
    --ink-light: #ffffff;
    --ink-soft: #e6e6e6;
    --accent: #8dc63f;
    --band-gray: #595a5c;
  }
  * { margin: 0; padding: 0; box-sizing: border-box; }
  html, body {
    width: 1200px; height: 900px; overflow: hidden;
    background: var(--backdrop);
    font-family: "Barlow", Arial, sans-serif;
  }
  .stage {
    width: 1200px; height: 900px;
    display: flex; align-items: center; justify-content: center; gap: 50px;
  }
  .card {
    position: relative;
    width: 525px; height: 300px;
    overflow: hidden;
  }

  /* Front */
  .card--front { background: var(--card-dark); color: var(--ink-light); }
  .front-brand {
    position: absolute; left: 0; right: 0; top: 92px;
    display: flex; align-items: center; justify-content: center; gap: 12px;
  }
  .brand-square { width: 26px; height: 26px; background: var(--accent); flex: none; }
  .front-brand .brand-name {
    font-size: 36px; font-weight: 500; letter-spacing: 0.5px;
    text-transform: uppercase; color: var(--ink-light);
  }
  .front-tagline {
    position: absolute; left: 12px; right: 12px; top: 178px;
    text-align: center;
  }
  .front-tagline .headline {
    color: var(--accent); font-size: 15px; font-weight: 500; letter-spacing: 0.8px;
  }
  .front-tagline .services {
    margin-top: 6px; font-size: 11px; letter-spacing: 0.4px; color: var(--ink-soft);
    white-space: nowrap;
  }

  /* Back */
  .card--back { background: var(--card-light); color: var(--ink-dark); }
  .back-brand {
    position: absolute; left: 36px; top: 40px;
    display: flex; align-items: center; gap: 10px;
  }
  .back-brand .brand-square { width: 18px; height: 18px; }
  .back-brand .brand-name {
    font-size: 22px; font-weight: 500; text-transform: uppercase;
    color: var(--ink-dark); letter-spacing: 0.3px;
  }
  .contact {
    position: absolute; left: 36px; top: 100px;
    text-transform: uppercase; font-size: 12px; line-height: 1.5; letter-spacing: 0.4px;
  }
  .contact .person { font-size: 17px; font-weight: 500; margin-bottom: 6px; }
  .contact .person .surname { color: var(--accent); }
  .address {
    position: absolute; left: 290px; top: 196px;
    font-style: normal;
    text-transform: uppercase; font-size: 12px; line-height: 1.5; letter-spacing: 0.4px;
  }
  .base-band {
    position: absolute; left: 0; bottom: 0; height: 16px; width: 100%;
    display: flex; gap: 4px;
  }
  .base-band .band-gray { flex: 0 0 72%; background: var(--band-gray); }
  .base-band .band-green { flex: 1; background: var(--accent); }
</style>
</head>
<body>
  <main class="stage">
    <section class="card card--front" aria-label="Card front">
      <div class="front-brand">
        <span class="brand-square"></span>
        <span class="brand-name">TerraLume Systems</span>
      </div>
      <div class="front-tagline">
        <p class="headline">EXPLORE YOUR DATA</p>
        <p class="services">SEAMLESS DATA SHARING . EFFECTIVE COLLABORATION . CONFIDENT DECISION-MAKING</p>
      </div>
    </section>

    <section class="card card--back" aria-label="Card back">
      <div class="back-brand">
        <span class="brand-square"></span>
        <span class="brand-name">TerraLume Systems</span>
      </div>
      <div class="contact">
        <p class="person">Harlan <span class="surname">Pike</span></p>
        <p>555.987.6543</p>
        <p>harlan@terralume-example.com</p>
        <p>www.terralume-example.com</p>
      </div>
      <address class="address">
        <p>Suite 720</p>
        <p>482 Birchmont Avenue SW</p>
        <p>Calgary, AB, Canada, T3K 4R8</p>
      </address>
      <div class="base-band">
        <span class="band-gray"></span>
        <span class="band-green"></span>
      </div>
    </section>
  </main>
</body>
</html>
```